Thornfield Marsh, LLC Website

We are a small law firm in need of a website that contains the following:
1. Attractive main page
2. About us/attorney info for three people: Leonard Thornfield (attorney), Brent Marsh (attorney), and Melinda Carrow (legal assistant). We have bio's ready to submit.
3. Blog/video page. We'd like to post blogs and videos to help drive traffic
4. Multidistrict Litigation and Class Actions page, where we post information regarding active MDLs and Class actions that we are doing intake on.
Updates

Can you also please use the color "gold" in the design and logo? Thanks.

Industry/Entity Type

Legal

Coding

Coded - Design and coding required

Number of Pages Required

1 page

Colors
0054AA
0677BA
7BADD7
CADEEF
E8F1F8

Requirements
Must have
• 1. Attractive main page 2. About us/attorney info for three people: Leonard Thornfield (attorney), Brent Marsh (attorney), and Melinda Carrow (legal assistant). We have bio's ready to submit. 3. Blog/video page. We'd like to post blogs and videos to help drive traffic 4. Multidistrict Litigation and Class Actions page, where we post information regarding active MDLs and Class actions that we are doing intake on.

```html
<!DOCTYPE html>
<html lang="en">
<head>
<meta charset="utf-8">
<title>Thornfield Marsh LLC — Professional Legal Representation</title>
<link href="https://fonts.googleapis.com/css2?family=Playfair+Display:wght@600;700&family=Source+Sans+3:wght@400;600;700&display=swap" rel="stylesheet">
<style>
:root{
  --gold:#d4ae3a;
  --navy:#2b3a4e;
  --navy-deep:#232f40;
  --ink:#2c3646;
  --text:#4a5260;
  --soft:#f6f7f9;
  --white:#ffffff;
  --field:#1e2733;
}
*{margin:0;padding:0;box-sizing:border-box}
html,body{width:709px;height:1200px;overflow:hidden}
body{position:relative;background:var(--white);font-family:"Source Sans 3",sans-serif;color:var(--text)}
.abs{position:absolute}
.serif{font-family:"Playfair Display",serif}
.center{text-align:center}

/* header */
.site-header{left:0;top:0;width:709px;height:37px;background:var(--white)}
.brand{left:139px;top:9px;display:flex;align-items:center;gap:4px}
.brand-mark{width:11px;height:11px;background:var(--gold)}
.brand-name{font-weight:700;font-size:8.5px;color:var(--gold);letter-spacing:.2px}
.main-nav{left:291px;top:13px;display:flex;gap:9px;font-size:5.2px;font-weight:600;letter-spacing:.2px;color:var(--ink)}
.main-nav .active{color:var(--gold);border-bottom:1px solid var(--gold);padding-bottom:2px}
.header-phone{left:524px;top:13px;font-size:5.4px;color:var(--ink);display:flex;align-items:center;gap:3px}

/* hero */
.hero{left:0;top:37px;width:709px;height:221px;background:linear-gradient(100deg,#2a2622 0%,#3d3832 45%,#4a433a 70%,#2a2724 100%)}
.hero-title-gold{left:0;top:88px;width:709px;font-size:23px;color:var(--gold);font-weight:700}
.hero-title-white{left:0;top:121px;width:709px;font-size:23px;color:var(--white);font-weight:700}
.hero-copy{left:212px;top:159px;width:285px;font-size:6.8px;line-height:11.4px;color:var(--white)}
.btn{background:var(--gold);color:var(--white);font-weight:700;letter-spacing:.4px;display:flex;align-items:center;justify-content:center}
.hero-btn{left:305px;top:194px;width:99px;height:18px;font-size:5.4px}

/* sections */
.band-soft{left:0;width:709px;background:var(--soft)}
.section-title{font-size:12.5px;color:var(--ink);font-weight:600}
.section-sub{font-size:5.4px}
.card{background:var(--white);box-shadow:0 1px 3px rgba(0,0,0,.08);text-align:center}
.card h3{font-family:"Playfair Display",serif;font-weight:600;font-size:10.5px;color:var(--ink)}
.card p{font-size:5.5px;line-height:9.5px;padding:0 12px}
.card .role{font-size:5.4px;font-weight:700;letter-spacing:.4px;color:var(--gold);line-height:9px}

.why-title{font-size:12.5px;color:var(--ink);font-weight:600}
.why-copy{font-size:5.5px;line-height:9.3px;width:215px}
.why-list{list-style:none;font-size:5.6px}
.why-list li{display:flex;align-items:center;gap:6px;height:14px}
.photo-office{background:linear-gradient(135deg,#6b4a2e 0%,#a8784a 35%,#c9a57a 55%,#8a5c36 80%,#3a2a20 100%)}

/* cta */
.cta{left:0;top:908px;width:709px;height:95px;background:linear-gradient(90deg,#232323 0%,#3a3936 50%,#2a2927 100%)}
.cta-title{left:0;top:917px;width:709px;font-size:12.5px;color:var(--white);font-weight:700}
.cta-copy{left:0;top:942px;width:709px;font-size:5.6px;color:var(--white)}
.cta-btn{left:320px;top:956px;width:69px;height:18px;font-size:5.4px}

/* footer */
.site-footer{left:0;top:1003px;width:709px;height:197px;background:var(--navy)}
.foot-title{font-size:10.5px;color:var(--white);font-weight:600}
.foot-rule{width:18px;height:1px;background:var(--gold)}
.foot-text{font-size:5.5px;color:var(--white);line-height:9.3px}
.foot-contact{font-size:5.5px;color:var(--white);display:flex;align-items:center;gap:5px}
.social{width:15px;height:15px;border-radius:50%;background:var(--navy-deep)}
.quick-links{list-style:none;font-size:5.5px;color:var(--white)}
.quick-links li{height:13.9px;display:flex;align-items:center;gap:4px}
.quick-links li::before{content:"";width:2px;height:2px;background:var(--gold)}
.form-panel{left:434px;top:1021px;width:136px;height:134px;background:var(--white)}
.field{background:var(--field);color:#b9c0ca;font-size:4.8px;padding:4px}
.legal-bar{left:139px;top:1167px;width:431px;height:33px;background:var(--navy-deep);font-size:5.5px;color:var(--white);display:flex;align-items:center;justify-content:center}
</style>
</head>
<body>

<header class="abs site-header">
  <div class="abs brand"><span class="brand-mark"></span><span class="brand-name">THORNFIELD MARSH LLC</span></div>
  <nav class="abs main-nav">
    <span class="active">HOME</span><span>ABOUT US</span><span>MDL &amp; CLASS ACTIONS</span><span>BLOG &amp; VIDEOS</span><span>CONTACT</span>
  </nav>
  <div class="abs header-phone">
    <svg width="6" height="6" viewBox="0 0 24 24"><path fill="#d4ae3a" d="M6.6 10.8a15 15 0 006.6 6.6l2.2-2.2a1 1 0 011-.25 11 11 0 003.6.6 1 1 0 011 1V20a1 1 0 01-1 1A17 17 0 013 4a1 1 0 011-1h3.5a1 1 0 011 1 11 11 0 00.6 3.6 1 1 0 01-.25 1z"/></svg>
    (555) 246-8013
  </div>
</header>

<section class="abs hero" role="img" aria-label="Dim law office with a lawyer signing papers, a framed certificate and a statue of Lady Justice"></section>
<h1 class="abs hero-title-gold serif center">Professional Legal</h1>
<h1 class="abs hero-title-white serif center">Representation</h1>
<p class="abs hero-copy center">Thornfield &amp; Associates Law Firm is dedicated to protecting your rights and providing expert legal counsel in Multidistrict Litigation and Class Actions.</p>
<a class="abs btn hero-btn">SCHEDULE A CONSULTATION</a>

<!-- expertise -->
<section class="abs band-soft" style="top:258px;height:204px"></section>
<h2 class="abs section-title serif center" style="left:0;top:289px;width:709px">Our Legal Expertise</h2>
<p class="abs section-sub center" style="left:0;top:314px;width:709px">We provide comprehensive legal services with a focus on Multidistrict Litigation and Class Actions.</p>

<div class="abs card" style="left:139px;top:328px;width:136px;height:104px">
  <svg class="abs" style="left:59px;top:11px" width="18" height="18" viewBox="0 0 24 24"><g fill="#d4ae3a"><rect x="11" y="2" width="8" height="6" rx="1" transform="rotate(45 15 5)"/><rect x="2" y="13" width="12" height="4" rx="1" transform="rotate(-45 8 15)"/></g></svg>
  <h3 style="margin-top:36px">Multidistrict Litigation</h3>
  <p style="margin-top:5px">We represent clients in complex MDL cases involving defective products, dangerous drugs, and corporate misconduct.</p>
</div>
<div class="abs card" style="left:287px;top:328px;width:135px;height:104px">
  <svg class="abs" style="left:56px;top:11px" width="23" height="18" viewBox="0 0 30 24"><g fill="#d4ae3a"><circle cx="15" cy="6" r="4.5"/><circle cx="6" cy="7" r="3.5"/><circle cx="24" cy="7" r="3.5"/><path d="M7 22a8 8 0 0116 0z"/><path d="M0 18a6 6 0 0110-3 10 10 0 00-3 3z"/><path d="M30 18a6 6 0 00-10-3 10 10 0 013 3z"/></g></svg>
  <h3 style="margin-top:36px">Class Action Lawsuits</h3>
  <p style="margin-top:5px">Our attorneys have extensive experience in class action lawsuits that seek justice for large groups of affected individuals.</p>
</div>
<div class="abs card" style="left:434px;top:328px;width:136px;height:104px">
  <svg class="abs" style="left:59px;top:11px" width="18" height="18" viewBox="0 0 24 24"><g fill="#d4ae3a"><path d="M8 4h8v3h-2V6h-4v1H8z"/><rect x="1" y="7" width="22" height="6" rx="1"/><rect x="1" y="14" width="22" height="8" rx="1"/><rect x="10" y="11" width="4" height="4" fill="#fff"/></g></svg>
  <h3 style="margin-top:36px">Personal Injury</h3>
  <p style="margin-top:5px">We fight for fair compensation for those who have been injured due to negligence or intentional harm.</p>
</div>

<!-- why choose -->
<h2 class="abs why-title serif" style="left:139px;top:492px">Why Choose Thornfield &amp; Associates?</h2>
<p class="abs why-copy" style="left:139px;top:516px">At Thornfield &amp; Associates, we combine extensive legal expertise with a client-centered approach to deliver exceptional results.</p>
<ul class="abs why-list" style="left:139px;top:539px">
  <li><svg width="6" height="6" viewBox="0 0 24 24"><path d="M3 12l6 6L21 6" stroke="#d4ae3a" stroke-width="3" fill="none"/></svg>Extensive experience in complex litigation</li>
  <li><svg width="6" height="6" viewBox="0 0 24 24"><path d="M3 12l6 6L21 6" stroke="#d4ae3a" stroke-width="3" fill="none"/></svg>Personalized attention to every case</li>
  <li><svg width="6" height="6" viewBox="0 0 24 24"><path d="M3 12l6 6L21 6" stroke="#d4ae3a" stroke-width="3" fill="none"/></svg>Commitment to maximizing client recovery</li>
  <li><svg width="6" height="6" viewBox="0 0 24 24"><path d="M3 12l6 6L21 6" stroke="#d4ae3a" stroke-width="3" fill="none"/></svg>Track record of successful verdicts and settlements</li>
  <li><svg width="6" height="6" viewBox="0 0 24 24"><path d="M3 12l6 6L21 6" stroke="#d4ae3a" stroke-width="3" fill="none"/></svg>No fee unless we win your case</li>
</ul>
<a class="abs btn" style="left:139px;top:618px;width:85px;height:18px;font-size:5.4px">LEARN MORE ABOUT US</a>
<div class="abs photo-office" style="left:360px;top:491px;width:210px;height:140px" role="img" aria-label="Smiling attorney in a grey suit signing documents at a wooden desk with flags and bookshelves"></div>

<!-- our team -->
<section class="abs band-soft" style="top:651px;height:110px"></section>
<div class="abs card" style="left:139px;top:662px;width:136px;height:74px">
  <h3 style="margin-top:8px">Leonard Thornfield</h3>
  <div class="role" style="margin-top:2px">ATTORNEY</div>
  <p style="margin-top:3px">Leads our MDL practice, guiding clients through complex product and drug litigation.</p>
</div>
<div class="abs card" style="left:287px;top:662px;width:135px;height:74px">
  <h3 style="margin-top:8px">Brent Marsh</h3>
  <div class="role" style="margin-top:2px">ATTORNEY</div>
  <p style="margin-top:3px">Focuses on class actions and personal injury claims, from intake through settlement.</p>
</div>
<div class="abs card" style="left:434px;top:662px;width:136px;height:74px">
  <h3 style="margin-top:8px">Melinda Carrow</h3>
  <div class="role" style="margin-top:2px">LEGAL ASSISTANT</div>
  <p style="margin-top:3px">Coordinates case intake, client records and communication for every matter we handle.</p>
</div>

<!-- active MDLs and class actions -->
<h2 class="abs why-title serif" style="left:139px;top:784px">Active MDLs &amp; Class Actions</h2>
<p class="abs why-copy" style="left:139px;top:808px">We are currently accepting intake on the following matters. Contact us to learn whether you may qualify.</p>
<ul class="abs why-list" style="left:139px;top:830px">
  <li><svg width="6" height="6" viewBox="0 0 24 24"><path d="M3 12l6 6L21 6" stroke="#d4ae3a" stroke-width="3" fill="none"/></svg>Defective medical implant MDL — accepting intake</li>
  <li><svg width="6" height="6" viewBox="0 0 24 24"><path d="M3 12l6 6L21 6" stroke="#d4ae3a" stroke-width="3" fill="none"/></svg>Prescription drug side effects MDL — accepting intake</li>
  <li><svg width="6" height="6" viewBox="0 0 24 24"><path d="M3 12l6 6L21 6" stroke="#d4ae3a" stroke-width="3" fill="none"/></svg>Consumer data breach class action — reviewing claims</li>
  <li><svg width="6" height="6" viewBox="0 0 24 24"><path d="M3 12l6 6L21 6" stroke="#d4ae3a" stroke-width="3" fill="none"/></svg>Contaminated water exposure — reviewing claims</li>
  <li><svg width="6" height="6" viewBox="0 0 24 24"><path d="M3 12l6 6L21 6" stroke="#d4ae3a" stroke-width="3" fill="none"/></svg>Unpaid wage class action — accepting intake</li>
</ul>
<div class="abs photo-office" style="left:360px;top:783px;width:210px;height:112px" role="img" aria-label="Attorney reviewing case files at a wooden desk"></div>

<!-- call to action -->
<section class="abs cta" role="img" aria-label="Dark background of legal papers and a scales of justice stamp"></section>
<h2 class="abs cta-title serif center">Ready to Discuss Your Case?</h2>
<p class="abs cta-copy center">Contact us today for a free, no-obligation consultation with one of our experienced attorneys.</p>
<a class="abs btn cta-btn">CONTACT US NOW</a>

<!-- footer -->
<footer class="abs site-footer"></footer>
<h3 class="abs foot-title serif" style="left:139px;top:1023px">Thornfield Marsh LLC</h3>
<div class="abs foot-rule" style="left:139px;top:1042px"></div>
<p class="abs foot-text" style="left:139px;top:1051px;width:130px">Professional legal representation dedicated to protecting your rights and interests.</p>
<div class="abs foot-contact" style="left:139px;top:1081px">
  <svg width="6" height="6" viewBox="0 0 24 24"><path fill="#d4ae3a" d="M6.6 10.8a15 15 0 006.6 6.6l2.2-2.2a1 1 0 011-.25 11 11 0 003.6.6 1 1 0 011 1V20a1 1 0 01-1 1A17 17 0 013 4a1 1 0 011-1h3.5a1 1 0 011 1 11 11 0 00.6 3.6 1 1 0 01-.25 1z"/></svg>(555) 246-8013</div>
<div class="abs foot-contact" style="left:139px;top:1093px">
  <svg width="6" height="6" viewBox="0 0 24 24"><rect x="2" y="5" width="20" height="14" fill="#d4ae3a"/><path d="M2 6l10 7 10-7" stroke="#2b3a4e" stroke-width="2" fill="none"/></svg>contact@thornfieldmarsh.com</div>
<div class="abs foot-contact" style="left:139px;top:1106px">
  <svg width="6" height="6" viewBox="0 0 24 24"><path fill="#d4ae3a" d="M12 2a7 7 0 00-7 7c0 5 7 13 7 13s7-8 7-13a7 7 0 00-7-7zm0 9.5A2.5 2.5 0 1112 6.5a2.5 2.5 0 010 5z"/></svg>450 Harbor Street, Suite 210, City, State 54321</div>
<div class="abs social" style="left:139px;top:1122px" aria-label="Social profile"></div>
<div class="abs social" style="left:158px;top:1122px" aria-label="Social profile"></div>
<div class="abs social" style="left:177px;top:1122px" aria-label="Social profile"></div>
<div class="abs social" style="left:196px;top:1122px" aria-label="Social profile"></div>

<h3 class="abs foot-title serif" style="left:287px;top:1023px">Quick Links</h3>
<div class="abs foot-rule" style="left:287px;top:1042px"></div>
<ul class="abs quick-links" style="left:287px;top:1049px">
  <li>Home</li><li>About Us</li><li>MDL &amp; Class Actions</li><li>Blog &amp; Videos</li><li>Contact</li>
</ul>

<div class="abs form-panel">
  <div class="abs foot-rule" style="left:12px;top:33px"></div>
  <div class="abs field" style="left:12px;top:42px;width:112px;height:14px">Your email address</div>
  <div class="abs field" style="left:12px;top:63px;width:112px;height:36px;font-family:monospace">Message</div>
  <a class="abs btn" style="left:12px;top:108px;width:112px;height:14px;font-size:5.4px">SEND</a>
</div>

<div class="abs legal-bar">© 2025 Thornfield Marsh LLC | All Rights Reserved</div>

</body>
</html>
```